Corvale Homes

To produce a business card design for our newly established house building and development company, We have had a logo design done please see attached, our slogan is "building your home sweet home"
Contact Information for Business Card
Adress on card needs to Read - 58 Elmsworth Lane, Kettering, Northamptonshire NN16 4QT. Director name Dean Vascotti
Requirements
Must have
- Web adress is www.corvale-homes.co.uk
- Email address is info@corvale-homes.co.uk
- phone number 07700 900417

```html
<!DOCTYPE html>
<html lang="en">
<head>
<meta charset="utf-8">
<title>Corvale Homes – Business Card</title>
<link rel="stylesheet" href="https://fonts.googleapis.com/css2?family=Lato:wght@400;700;900&display=swap">
<style>
  :root {
    --stage: #000000;
    --card: #ffffff;
    --leaf: #8cc63f;
    --slate: #999999;
    --ink: #1f1f1f;
  }
  html, body {
    margin: 0;
    padding: 0;
    width: 1200px;
    height: 1200px;
    overflow: hidden;
    background: var(--stage);
  }
  .canvas {
    position: relative;
    width: 1200px;
    height: 1200px;
    background: var(--stage);
    font-family: "Lato", sans-serif;
  }
  .card {
    position: absolute;
    left: 197px;
    width: 822px;
    height: 470px;
    background: var(--card);
    overflow: hidden;
  }
  .card--front { top: 76px; }
  .card--back  { top: 623px; }
  .card__roof {
    position: absolute;
    inset: 0;
    width: 100%;
    height: 100%;
    display: block;
  }
  .roof-fill { fill: var(--leaf); }
  .roof-band { fill: var(--slate); }
  .card__details {
    position: absolute;
    margin: 0;
    color: var(--ink);
    font-size: 24px;
    line-height: 1.2;
    font-weight: 400;
  }
  .card__details p { margin: 0; white-space: nowrap; }
  .card--front .card__details { left: 431px; top: 30px; }
  .card--front .detail-gap { margin-top: 40px; }
  .card--back .card__details { left: 74px; top: 48px; line-height: 35px; }
  .brand-name {
    position: absolute;
    margin: 0;
    color: var(--leaf);
    font-weight: 900;
    font-size: 40px;
    letter-spacing: 1px;
    text-transform: uppercase;
    white-space: nowrap;
    transform: translate(-50%, -50%);
  }
  .card--front .brand-name { left: 225px; top: 330px; }
  .card--back .brand-name  { left: 577px; top: 345px; }
</style>
</head>
<body>
<main class="canvas">

  <section class="card card--front" aria-label="Business card front">
    <svg class="card__roof" viewBox="0 0 714 408" preserveAspectRatio="none" aria-hidden="true">
      <polygon class="roof-fill" points="59,0 714,0 714,343 610,289 610,164 477,164 477,219"/>
      <polygon class="roof-band" points="0,0 59,0 477,219 477,164 610,164 610,289 714,343 714,374 576,302 576,201 512,201 512,268"/>
    </svg>
    <div class="card__details">
      <p>58 Elmsworth Lane, Kettering</p>
      <p>Northamptonshire NN16 4QT</p>
      <p class="detail-gap">Director Dean Vascotti</p>
    </div>
    <p class="brand-name">Corvale Homes</p>
  </section>

  <section class="card card--back" aria-label="Business card back">
    <svg class="card__roof" viewBox="0 0 714 408" preserveAspectRatio="none" aria-hidden="true">
      <polygon class="roof-fill" points="0,0 657,0 237,220 237,164 103,164 103,290 0,344"/>
      <polygon class="roof-band" points="657,0 714,0 201,269 201,200 138,200 138,302 0,374 0,344 103,290 103,164 237,164 237,220"/>
    </svg>
    <div class="card__details">
      <p>www.corvale-homes.co.uk</p>
      <p>email - info@corvale-homes.co.uk</p>
      <p>phone-07700 900417</p>
    </div>
    <p class="brand-name">Corvale Homes</p>
  </section>

</main>
</body>
</html>
```